Velmora Brightstead Website

Create website for Legal Management Company which specializes in Law Office Spersriinal Management
System implementation & Training
Global presence
Paralegal Services - Remote or In-Office
Legal Research
- Judge Motion Ruling History
- Opposing Counsel Opposition Research - Historical Filings - Pattern identification
Service by Mail - Ex- Parte Notice

Probate -Heir Finder - Asset Location -

```html
<!DOCTYPE html>
<html lang="en">
<head>
<meta charset="UTF-8">
<title>Velmora Brightstead — Legal Management</title>
<link href="https://fonts.googleapis.com/css2?family=Playfair+Display:ital,wght@0,500;0,600;1,500;1,600&family=Work+Sans:wght@400;500;600;700&display=swap" rel="stylesheet">
<style>
:root{
  --brown-900:#21140d;
  --brown-800:#2e1c12;
  --brown-700:#4a2f1f;
  --brown-600:#5e3d28;
  --brown-400:#8a6a52;
  --gold:#f0b43c;
  --cream:#f4f2ef;
  --grey-band:#ececec;
  --ink:#1d1d1d;
  --muted:#666;
  --line:#e2e2e2;
  --white:#fff;
}
*{box-sizing:border-box;margin:0;padding:0}
html,body{width:1200px;height:4788px;overflow:hidden}
body{font-family:"Work Sans",Arial,sans-serif;color:var(--ink);background:var(--white);position:relative}
.serif{font-family:"Playfair Display",Georgia,serif;font-style:italic;font-weight:500}
section,header,footer{position:relative;width:1200px}
.abs{position:absolute}
.label{font-size:15px;font-weight:500;display:flex;align-items:center;gap:10px}
.label::before{content:"";width:7px;height:7px;border-radius:50%;background:var(--gold)}
.pill{display:inline-flex;align-items:center;gap:8px;background:var(--brown-700);color:var(--white);font-size:13px;font-weight:500;padding:11px 22px;border-radius:30px}
.para{font-size:13px;line-height:1.7;color:#444}

/* hero */
.hero{height:680px;background:radial-gradient(ellipse at 50% 35%,#7a5a44 0%,#4a3122 45%,#21140d 100%);color:var(--white)}
.nav{left:80px;right:80px;top:34px;height:36px;display:flex;align-items:center;justify-content:space-between}
.brand{font-size:20px;font-weight:600;color:var(--white)}
.nav-links{display:flex;gap:24px;font-size:12px}
.nav-links span:first-child{color:var(--gold)}
.nav-cta{font-size:12px;display:flex;align-items:center;gap:8px}
.hero-photo{left:0;top:0;width:1200px;height:680px}
.hero-title{left:0;right:0;top:420px;text-align:center;font-size:52px;line-height:1.12}
.hero-title .serif{display:block;font-size:56px}
.hero-title b{font-weight:600}
.hero-strip{left:80px;right:80px;top:626px;display:flex;justify-content:space-between;font-size:12px;font-weight:500}

/* about */
.about{height:720px}
.about h2{left:560px;font-size:34px;font-weight:600;line-height:1.2}
.about-photo{left:210px;width:270px;height:205px;border-radius:18px;background:linear-gradient(135deg,#9a7a62,#4d3425)}
.about-text{left:580px;width:450px}

/* services */
.services{height:720px;background:linear-gradient(180deg,#2a1810,#3b2418 50%,#22140d);color:var(--white);overflow:hidden}
.services h2{left:400px;font-size:32px;font-weight:600;line-height:1.2}
.arrows{left:955px;display:flex;gap:18px}
.arrow-btn{width:44px;height:44px;border-radius:50%;border:1.5px solid var(--white);display:flex;align-items:center;justify-content:center}
.arrow-btn.on{background:var(--white)}
.cards{left:150px;display:flex;gap:20px}
.card{width:222px;height:300px;border-radius:14px;background:rgba(255,255,255,.09);padding:80px 20px 0}
.card h3{font-size:17px;font-weight:600;line-height:1.35;margin-bottom:22px}
.card li{list-style:none;font-size:11px;line-height:1.5;margin-bottom:6px;padding-left:12px;position:relative}
.card li::before{content:"•";position:absolute;left:0}
.services-note{left:0;right:0;text-align:center;font-size:12px}
.services-note u{margin-left:4px}

/* global */
.global{height:600px}
.global h2{left:520px;font-size:32px;font-weight:600;line-height:1.2}
.global-text{left:170px;width:250px}
.map{left:520px;width:510px;height:220px;border-radius:10px;background:linear-gradient(135deg,#ececec,#d6d2cd)}

/* insights */
.insights{height:440px;background:var(--grey-band)}
.insights-photo{left:185px;width:320px;height:265px;border-radius:16px;background:linear-gradient(135deg,#3d2a1f,#8d7260 60%,#c7b7a7)}
.insights h2{left:580px;font-size:32px;font-weight:600}

/* reviews */
.reviews{height:880px}
.reviews h2{left:170px;font-size:34px;font-weight:600;line-height:1.15}
.badge{display:flex;align-items:center;gap:10px;font-size:11px}
.badge-mark{width:34px;height:34px;border-radius:50%;background:#d7d7d7}
.stars{color:var(--gold);letter-spacing:1px;font-size:12px}
.review-row{left:160px;width:880px;height:440px;display:flex;border-top:1px solid var(--line)}
.review{flex:1;text-align:center;padding:30px 30px 0;border-right:1px solid var(--line)}
.review:last-child{border-right:none}
.avatar{width:52px;height:52px;border-radius:50%;margin:0 auto 50px;background:linear-gradient(135deg,#8b6a52,#3b2719)}
.review p{font-size:13px;line-height:1.7;color:#444;margin-bottom:40px}
.review-name{font-size:13px;font-weight:600;margin-bottom:6px}

/* contact + footer */
.footer{height:640px;background:var(--brown-800);color:var(--white)}
.contact-card{left:135px;top:4040px;width:930px;height:380px;border-radius:28px;background:var(--cream);box-shadow:0 0 0 1px #ddd;color:var(--ink)}
.contact-card h2{position:absolute;left:50px;top:105px;font-size:36px}
.contact-card .para{position:absolute;left:50px;top:160px;width:260px;font-size:12px}
.contact-card .pill{position:absolute;left:50px;top:230px}
.form{position:absolute;left:490px;top:40px;width:360px;height:300px;background:var(--white);border-radius:18px;padding:30px 40px}
.field{height:32px;border-radius:16px;background:#ececec;margin-bottom:12px;font-size:11px;color:#888;padding:9px 16px}
.field.tall{height:48px}
.form .pill{position:static;width:100%;justify-content:center;margin-top:4px}
.f-brand{left:90px;top:4585px;font-size:26px;font-weight:600}
.socials{left:90px;top:4645px;display:flex;gap:12px}
.socials span{width:32px;height:32px;border-radius:50%;border:1px solid rgba(255,255,255,.6)}
.f-col{top:4545px;font-size:12px;line-height:1.9}
.f-col h4{font-size:14px;font-weight:600;margin-bottom:10px}
.contact-line{display:flex;gap:8px;align-items:flex-start;margin-bottom:6px;line-height:1.5}
.news-input{margin-top:14px;width:220px;height:36px;border-radius:18px;background:rgba(255,255,255,.12);display:flex;align-items:center;justify-content:space-between;padding:0 6px 0 16px;font-size:11px}
.news-input i{width:26px;height:26px;border-radius:50%;background:var(--gold)}
.copyright{left:0;right:0;top:4742px;text-align:center;font-size:11px;border-top:1px solid rgba(255,255,255,.15);padding-top:10px}
.to-top{left:1142px;top:4740px;width:36px;height:36px;border-radius:50%;background:var(--gold)}
</style>
</head>
<body>

<header class="hero">
  <div class="abs hero-photo" role="img" aria-label="Group portrait of four legal professionals in business attire"></div>
  <nav class="abs nav">
    <span class="brand">Velmora Brightstead</span>
    <div class="nav-links"><span>Home</span><span>About Us</span><span>Services</span><span>Global Presence</span><span>Insights / Research</span><span>Contact</span></div>
    <span class="nav-cta">Schedule a Consultation →</span>
  </nav>
  <h1 class="abs hero-title"><span class="serif">Empowering Law Firms</span><b>with Precision, Insight &amp;<br>Efficiency</b></h1>
  <div class="abs hero-strip"><span>Learn More →</span><span>Specialized Legal Management Solutions | Paralegal Services | Research &amp; Strategic Insights — Globally</span><span>Get Started →</span></div>
</header>

<section class="about">
  <div class="abs label" style="left:220px;top:140px">About</div>
  <h2 class="abs" style="top:130px">Velmora Brightstead —<br><span class="serif">Legal Management</span> Experts</h2>
  <div class="abs about-photo" style="top:300px" role="img" aria-label="Legal team gathered in a law office"></div>
  <div class="abs about-text" style="top:325px">
    <p class="para">Velmora Brightstead is a global legal management company dedicated to optimizing law office operations through specialized system implementation, professional training, and strategic legal support. Our mission is to empower law firms with the tools, insights, and expertise needed to operate efficiently and deliver exceptional results.</p>
    <p class="para" style="margin-top:14px">Our mission is to empower law firms with the insights, tools, and expertise necessary to operate seamlessly, make informed decisions, and achieve exceptional results for their clients.</p>
    <span class="pill" style="margin-top:22px">Read More About Us ↗</span>
  </div>
</section>

<section class="services">
  <div class="abs label" style="left:150px;top:110px">Our Services</div>
  <h2 class="abs" style="top:80px">Comprehensive<br><span class="serif">Legal Management</span> Solutions</h2>
  <div class="abs arrows" style="top:97px">
    <span class="arrow-btn"><svg width="14" height="14" viewBox="0 0 14 14"><path d="M9 2 4 7l5 5" stroke="#fff" stroke-width="1.6" fill="none"/></svg></span>
    <span class="arrow-btn on"><svg width="14" height="14" viewBox="0 0 14 14"><path d="M5 2l5 5-5 5" stroke="#2e1c12" stroke-width="1.6" fill="none"/></svg></span>
  </div>
  <div class="abs cards" style="top:220px">
    <div class="card"><h3>Law Office<br>Management System</h3><ul><li>Implementation of tailored legal management systems</li><li>Staff training for seamless adoption</li><li>Workflow optimization for efficiency</li></ul></div>
    <div class="card"><h3>Legal Research<br>&amp; Insights</h3><ul><li>Comprehensive case law and statute research</li><li>Historical motion ruling analysis</li><li>Pattern identification for judges and opposing counsel</li></ul></div>
    <div class="card"><h3>Paralegal<br>Solutions Services</h3><ul><li>Remote paralegals for research, filing, and support</li><li>In-office paralegals for day-to-day operations</li><li>Flexible engagement models</li></ul></div>
    <div class="card"><h3>Service by Mail —<br>Ex-Parte Notice</h3><ul><li>Delivery of legal notices by mail</li><li>Handling ex-parte procedural requirements</li></ul></div>
  </div>
  <p class="abs services-note" style="top:610px">We invite you to take a step for more information. <u>View All Services</u> ↗</p>
</section>

<section class="global">
  <div class="abs label" style="left:170px;top:70px">Global Presence</div>
  <h2 class="abs" style="top:40px"><span class="serif">Our Global Reach</span> — Supporting<br>Law Firms Worldwide</h2>
  <p class="abs para global-text" style="top:210px">Velmora Brightstead operates across multiple countries, delivering expert legal management and paralegal solutions to law firms around the globe. Our international presence ensures that your firm has access to reliable, professional support wherever it is needed, helping you to operate efficiently across borders and jurisdictions.</p>
  <div class="abs map" style="top:220px" role="img" aria-label="World map showing global office locations"></div>
</section>

<section class="insights">
  <div class="abs insights-photo" style="top:80px" role="img" aria-label="Attorney reviewing case research at a desk"></div>
  <h2 class="abs" style="top:150px">Strategic <span class="serif">Legal Insights</span></h2>
  <p class="abs para" style="left:580px;top:202px;width:460px;font-size:12px;line-height:1.6">We provide data-driven legal intelligence to support your case strategy. From judge ruling histories to opposing counsel analysis, our research helps you make informed decisions and anticipate challenges before they arise.</p>
  <span class="abs pill" style="left:580px;top:285px">Request a Research Consultation ↗</span>
</section>

<section class="reviews">
  <div class="abs label" style="left:170px;top:140px">Clients Review</div>
  <h2 class="abs" style="top:175px">Trusted by 15,000+<br><span class="serif">happy customers</span></h2>
  <div class="abs badge" style="left:760px;top:185px"><span class="badge-mark"></span><div><div class="stars">★★★★★</div><u>134 Review</u></div></div>
  <div class="abs badge" style="left:900px;top:185px"><span class="badge-mark"></span><div><div class="stars">★★★★★</div><u>138 Review</u></div></div>
  <div class="abs review-row" style="top:320px">
    <div class="review"><div class="avatar" role="img" aria-label="Client portrait"></div><p>It is a long established fact that a reader will be distracted by the readable content of a page when looking at its layout. The point of using Lorem Ipsum is that it has a more-or-less normal distribution of letters, as opposed to using Content here.</p><div class="review-name">Dara Ellison</div><div class="stars">★★★★★</div></div>
    <div class="review"><div class="avatar" role="img" aria-label="Client portrait"></div><p>It is a long established fact that a reader will be distracted by the readable content of a page when looking at its layout. The point of using Lorem Ipsum is that it has a more-or-less normal distribution of letters, as opposed to using Content here.</p><div class="review-name">Dara Ellison</div><div class="stars">★★★★★</div></div>
    <div class="review"><div class="avatar" role="img" aria-label="Client portrait"></div><p>It is a long established fact that a reader will be distracted by the readable content of a page when looking at its layout. The point of using Lorem Ipsum is that it has a more-or-less normal distribution of letters, as opposed to using Content here.</p><div class="review-name">Dara Ellison</div><div class="stars">★★★★★</div></div>
  </div>
</section>

<footer class="footer" style="position:absolute;top:4148px;left:0"></footer>

<div class="abs contact-card">
  <h2 class="serif">Get <span style="font-style:normal;font-family:'Work Sans',sans-serif;font-weight:600">in Touch</span></h2>
  <p class="para">Connect with our experts to discuss your legal management needs, schedule a consultation, or request a tailored service package.</p>
  <span class="pill">Get a Free Quote ↗</span>
  <div class="form">
    <div class="field">Name</div>
    <div class="field">Email</div>
    <div class="field">Company / Law Firm</div>
    <div class="field tall">Message</div>
    <span class="pill">Submit Inquiry ↗</span>
  </div>
</div>

<div class="abs f-brand" style="color:#fff">Velmora Brightstead</div>
<div class="abs socials"><span></span><span></span><span></span><span></span></div>

<div class="abs f-col" style="left:410px;color:#fff">
  <h4>Quick Links</h4>
  <div>Home</div><div>About Us</div><div>Services</div><div>Global Presence</div><div>Insights / Research</div><div>Contact</div>
</div>

<div class="abs f-col" style="left:590px;color:#fff;width:200px">
  <h4>Contact Info</h4>
  <div class="contact-line"><svg width="14" height="14" viewBox="0 0 14 14"><rect x="1" y="3" width="12" height="8" rx="1" stroke="#f0b43c" fill="none"/><path d="M1 3l6 5 6-5" stroke="#f0b43c" fill="none"/></svg><span>Email<br>info@velmorabrightstead.com</span></div>
  <div class="contact-line"><svg width="14" height="14" viewBox="0 0 14 14"><path d="M3 1h3l1 3-2 1a7 7 0 0 0 4 4l1-2 3 1v3c-6 1-11-4-10-10z" stroke="#f0b43c" fill="none"/></svg><span>Phone<br>+00 000 000 0000</span></div>
  <div class="contact-line"><svg width="14" height="14" viewBox="0 0 14 14"><path d="M7 13s-4-4.5-4-7.5a4 4 0 0 1 8 0C11 8.5 7 13 7 13z" stroke="#f0b43c" fill="none"/><circle cx="7" cy="5.5" r="1.5" fill="#f0b43c"/></svg><span>Location<br>24 Harlow Street,<br>Clearview, State 0000</span></div>
</div>

<div class="abs f-col" style="left:840px;color:#fff">
  <h4>Newsletter</h4>
  <div style="width:200px;line-height:1.5">Subscribe to our email address to get the latest news.</div>
  <div class="news-input"><span>Enter your email...</span><i></i></div>
</div>

<div class="abs copyright" style="color:#fff">© Copyright 2025 Velmora Brightstead. All Rights Reserved.</div>
<div class="abs to-top"></div>

</body>
</html>
```